Stationary for a computer tech, hardware selling & website building & hosting for smb's
Pavillon Informatique
Professional
Mathieu Ostrowel
Directeur associé
4187 Boul. Lanvoisier Est
Montréal (Qc) H7T 8W2
514.555.0148 p.317
mathieu@pavillon-exemple.ca
www.pavillon-exemple.ca
Logo on white background
Logo on black background

```html
<!DOCTYPE html>
<html lang="fr">
<head>
<meta charset="utf-8">
<title>Pavillon Informatique – Cartes professionnelles</title>
<link href="https://fonts.googleapis.com/css2?family=Arimo:wght@400;700&display=swap" rel="stylesheet">
<style>
  :root {
    --green: #7cc12a;
    --charcoal: #474747;
    --ink: #333333;
    --white: #ffffff;
    --stage: #b4b4b4;
    --frame: #2a2a2a;
    --card-edge: #9a9a9a;
  }
  * { margin: 0; padding: 0; box-sizing: border-box; }
  html, body {
    width: 1200px; height: 715px; overflow: hidden;
    font-family: "Arimo", Arial, sans-serif;
  }
  .stage {
    position: relative; width: 1200px; height: 715px;
    background: var(--stage);
    border: 5px solid var(--frame);
  }
  .card {
    position: absolute; width: 504px; height: 290px;
    border-radius: 19px; overflow: hidden;
    border: 2px solid var(--card-edge);
  }
  .card--front { left: 74px; top: 48px; background: var(--white); }
  .card--green { left: 602px; top: 48px; background: var(--green); }
  .card--white { left: 74px; top: 362px; background: var(--white); }
  .card--dark  { left: 602px; top: 362px; background: var(--charcoal); }

  .brand { display: flex; align-items: center; gap: 10px; }
  .brand__dot { width: 40px; height: 40px; border-radius: 50%; flex: none; }
  .brand__name { font-weight: 700; font-size: 25px; letter-spacing: -0.3px; }

  .card--front .brand { position: absolute; left: 16px; top: 20px; }
  .card--front .brand__dot { background: var(--green); width: 46px; height: 46px; }
  .card--front .brand__name { color: var(--charcoal); }

  .front__accent {
    position: absolute; left: 410px; top: 34px;
    width: 220px; height: 220px; border-radius: 50%;
    background: var(--green);
  }

  .person { position: absolute; left: 90px; top: 116px; width: 320px; text-align: center; }
  .person__name { color: var(--green); font-weight: 700; font-size: 21px; }
  .person__title { color: var(--ink); font-size: 14px; margin-top: 4px; }

  .contact { position: absolute; left: 14px; top: 198px; font-size: 13.5px; line-height: 21.5px; color: var(--ink); }
  .contact__label { color: var(--green); }

  .centered { position: absolute; inset: 0; display: flex; align-items: center; justify-content: center; }
  .centered .brand { flex-direction: column; gap: 14px; }
  .centered .brand__dot { width: 96px; height: 96px; }
  .centered .brand__name { font-size: 26px; }

  .card--green .brand__dot { background: var(--white); }
  .card--green .brand__name { color: var(--white); }
  .card--white .brand__dot { background: var(--green); }
  .card--white .brand__name { color: var(--charcoal); }
  .card--dark .brand__dot { background: var(--white); }
  .card--dark .brand__name { color: var(--white); }
</style>
</head>
<body>
<main class="stage">
  <section class="card card--front" aria-label="Recto de la carte">
    <div class="front__accent"></div>
    <div class="brand">
      <span class="brand__dot"></span>
      <span class="brand__name">Pavillon Informatique</span>
    </div>
    <div class="person">
      <p class="person__name">Mathieu Ostrowel</p>
      <p class="person__title">Directeur associé</p>
    </div>
    <div class="contact">
      <p>4187 Boul. Lanvoisier Est, Montréal (Qc) H7T 8W2</p>
      <p><span class="contact__label">Cell:</span> 514.555.0192 | <span class="contact__label">Phone:</span> 514.555.0148 p.317</p>
      <p><span class="contact__label">Fax:</span> 514.555.0163</p>
      <p><span class="contact__label">Email:</span> mathieu@pavillon-exemple.ca | <span class="contact__label">www.pavillon-exemple.ca</span></p>
    </div>
  </section>

  <section class="card card--green" aria-label="Verso vert">
    <div class="centered">
      <div class="brand"><span class="brand__dot"></span><span class="brand__name">Pavillon Informatique</span></div>
    </div>
  </section>

  <section class="card card--white" aria-label="Logo sur fond blanc">
    <div class="centered">
      <div class="brand"><span class="brand__dot"></span><span class="brand__name">Pavillon Informatique</span></div>
    </div>
  </section>

  <section class="card card--dark" aria-label="Logo sur fond foncé">
    <div class="centered">
      <div class="brand"><span class="brand__dot"></span><span class="brand__name">Pavillon Informatique</span></div>
    </div>
  </section>
</main>
</body>
</html>
```